Creation of foldable A4 Leaflet to summarise my website

I need to summarize the content of my website into a 4 facecs-2 pages A4 foldable leaflet. I need the leaflet to go through the main topics of my website, with accurate descriptions and some pics taken from the website. Focusing about professionality and over 25 year experience on the field. Give also apace to our valued partners and customers
My website plimborex.au

Target Market(s)

Industrial filtration, dust collector business

Industry/Entity Type

Industrial filtration, dust collectors market, mining, powerplant, cement industry

Font styles to use
Sans Serif

Colors
0054AA
0677BA
7BADD7
CADEEF
E8F1F8

Requirements
Must have
• clear references to my website
Nice to have
• clear and clean layout
Should not have
• dark colours other than blue and navy, as per my logo

```html
<!DOCTYPE html>
<html lang="en">
<head>
<meta charset="UTF-8">
<title>Plimborex Leaflet Cover</title>
<link href="https://fonts.googleapis.com/css2?family=Montserrat:wght@500;600;700&display=swap" rel="stylesheet">
<style>
  :root {
    --blue-deep: #0054AA;
    --blue-mid: #0677BA;
    --blue-soft: #7BADD7;
    --blue-pale: #CADEEF;
    --blue-mist: #E8F1F8;
    --navy: #13294B;
    --backdrop: #221E20;
  }
  html, body {
    margin: 0;
    padding: 0;
    width: 1200px;
    height: 1000px;
    overflow: hidden;
    background: var(--backdrop);
    font-family: "Montserrat", sans-serif;
  }
  .leaflet-cover {
    position: absolute;
    left: 300px;
    top: 85px;
    width: 587px;
    height: 831px;
    background: var(--blue-pale);
    overflow: hidden;
  }
  .brand-header {
    position: absolute;
    left: 0; top: 0;
    width: 100%;
    height: 158px;
    display: flex;
    align-items: center;
    justify-content: center;
    gap: 12px;
  }
  .brand-mark {
    width: 26px;
    height: 26px;
    background: var(--blue-mid);
  }
  .brand-name {
    font-weight: 700;
    font-size: 26px;
    letter-spacing: 3px;
    color: var(--navy);
  }
  .hero-photo {
    position: absolute;
    left: 0; top: 158px;
    width: 100%;
    height: 539px;
    background:
      linear-gradient(180deg, rgba(160,190,225,0.9) 0%, rgba(160,190,225,0) 32%),
      linear-gradient(100deg, #b9a98a 0%, #a89a80 35%, #8f8a84 60%, #a4a8ad 80%, #7d8893 100%);
  }
  .headline-panel {
    position: absolute;
    left: 0; top: 314px;
    width: 474px;
    height: 220px;
    background: var(--blue-mist);
  }
  .headline {
    position: absolute;
    left: 47px; top: 28px;
    margin: 0;
    font-weight: 600;
    font-size: 38px;
    line-height: 56px;
    color: var(--blue-deep);
    white-space: nowrap;
  }
  .tagline-band {
    position: absolute;
    left: 0; top: 697px;
    width: 100%;
    height: 36px;
    background: var(--blue-mist);
    display: flex;
    align-items: center;
    justify-content: center;
  }
  .tagline {
    margin: 0;
    font-weight: 600;
    font-size: 16px;
    color: var(--navy);
    white-space: nowrap;
  }
  .site-url {
    position: absolute;
    left: 0; top: 757px;
    width: 100%;
    text-align: center;
    font-weight: 600;
    font-size: 25px;
    color: var(--blue-deep);
    margin: 0;
  }
</style>
</head>
<body>
  <main class="leaflet-cover">
    <header class="brand-header">
      <span class="brand-mark"></span>
      <span class="brand-name">PLIMBOREX</span>
    </header>

    <div class="hero-photo" role="img" aria-label="Industrial plant with dust collector ducting, steel structures and a blue boom lift under a cloudy sky"></div>

    <section class="headline-panel">
      <h1 class="headline">Over 25 Years of<br>Excellence in<br>Industrial Filtration</h1>
    </section>

    <div class="tagline-band">
      <p class="tagline">Premium Dust Collector Supply &amp; Expert Maintenance Solutions</p>
    </div>

    <p class="site-url">plimborex.au</p>
  </main>
</body>
</html>
```